Website for The Velvet Pathfinder

We need an impressive e-commerce website for our newly launched business "The Velvet Pathfinder".
The Velvet Pathfinder searches store-front and online retailers for diamond engagement rings according to the client's specified requirements. We want to save people time by doing the shopping around for them.
We can relate to, and we love, www.corvaline.com
Like corvaline.com, we want to offer website visitors a quick run-down on how the process works, then offer them to elect a service package and pay for that package on the spot.
Content pages:
HOME
HOW IT WORKS
DIAMOND GALLERY
ABOUT
FAQs
CONTACT
Inclusions: Our logo and Pathway and Instagram buttons
We want to be able to easily edit this website, We want it to display well on iPhone and android, We want it to be clean and striking.
Like our logo, we want our website to embody elegant masculinity.
Target Market(s)
Men in market for diamond ring purchase $5k - $50k
Industry/Entity Type
Business
Number of Pages Required
5+ page
Font styles to use
Look and feel

```html
<!DOCTYPE html>
<html lang="en">
<head>
<meta charset="utf-8">
<title>The Velvet Pathfinder</title>
<link href="https://fonts.googleapis.com/css2?family=Open+Sans:wght@300;400;600;700&display=swap" rel="stylesheet">
<style>
:root{
  --ink:#2b2b2b;
  --muted:#777;
  --line:#d9d9d9;
  --button:#555;
  --cream:#fbfaf3;
  --white:#fff;
  --silver-hi:#f7f7f7;
  --silver:#cfcfcf;
  --silver-lo:#a9a9a9;
  --gold:#d9c58a;
  --skin:#eac7b1;
}
*{margin:0;padding:0;box-sizing:border-box}
html,body{width:1200px;height:2703px;overflow:hidden}
body{font-family:"Open Sans",Arial,sans-serif;color:var(--ink);background:var(--white);position:relative}
.photo{position:absolute}

/* nav */
.topnav{position:absolute;left:0;top:0;width:1200px;height:48px;background:var(--white);z-index:2}
.topnav .links{position:absolute;left:132px;top:15px;display:flex;gap:31px;font-size:12px;color:#555}
.topnav .links .active{color:var(--ink);border-bottom:1px solid var(--ink);padding-bottom:3px}
.topnav .cart{position:absolute;right:132px;top:13px;font-size:12px;color:#444;display:flex;align-items:center;gap:10px}

/* hero */
.hero{position:absolute;left:0;top:48px;width:1200px;height:478px;overflow:hidden;
  background:linear-gradient(90deg,#e4e4e4 0%,#dadada 30%,#cfcfcf 100%)}
.hero .photo{left:0;top:0;width:1200px;height:478px;
  background:
    linear-gradient(160deg,rgba(217,197,138,0) 55%,rgba(217,197,138,.55) 64%,rgba(240,226,180,.7) 67%,rgba(217,197,138,0) 74%),
    linear-gradient(150deg,rgba(255,255,255,0) 38%,rgba(255,255,255,.7) 46%,rgba(190,190,190,.2) 54%,rgba(255,255,255,0) 60%),
    linear-gradient(90deg,rgba(228,228,228,0) 30%,rgba(190,190,190,.35) 60%,rgba(170,170,170,.25) 100%)}
.brandbox{position:absolute;left:132px;top:20px;width:200px;height:199px;background:var(--white)}
.brandbox .mark{position:absolute;top:38px;left:84px;width:32px;height:32px;border:2px solid #8a8a8a}
.brandbox .name{position:absolute;left:0;width:200px;top:116px;font-size:15px;line-height:19px;color:#5a5a5a;text-align:center;letter-spacing:1px;text-transform:uppercase}
.hero h1{position:absolute;left:132px;top:266px;font-weight:300;font-size:28px;line-height:36px;color:#333}
.btn-dark{position:absolute;left:132px;top:352px;width:199px;height:45px;background:var(--button);color:var(--white);font-size:15px;display:flex;align-items:center;justify-content:center}
.dots{position:absolute;left:570px;top:448px;display:flex;gap:7px}
.dots span{width:6px;height:6px;border-radius:50%;background:rgba(255,255,255,.6)}
.dots span.on{background:var(--white)}

/* how it works */
.how{position:absolute;left:0;top:526px;width:1200px;height:402px;background:var(--cream);overflow:hidden}
.how .photo{left:0;top:0;width:620px;height:402px;
  background:
    linear-gradient(150deg,rgba(80,80,80,0) 0%,rgba(80,80,80,0) 22%,rgba(70,70,70,.55) 24%,rgba(70,70,70,0) 27%),
    linear-gradient(180deg,rgba(251,250,243,0) 40%,rgba(200,200,200,.45) 75%,rgba(225,225,225,.5) 100%),
    linear-gradient(90deg,#dcdcd8 0%,#e9e9e4 40%,rgba(251,250,243,0) 100%)}
.section-title{font-size:14px;letter-spacing:.5px;text-transform:uppercase;color:#333;border-bottom:2px solid #333;padding-bottom:4px;display:inline-block}
.how .section-title{position:absolute;left:540px;top:28px}
.how .lead{position:absolute;left:0;width:1200px;top:66px;text-align:center;font-size:12.5px;color:#666}
.step{position:absolute;left:600px;display:flex;align-items:center;gap:20px}
.step .icon{width:64px;height:64px;border-radius:50%;background:#555;display:flex;align-items:center;justify-content:center}
.step h3{font-weight:400;font-size:15.5px;color:#333;letter-spacing:.3px}
.step p{font-size:10.5px;color:#666;margin-top:1px}

/* products */
.products{position:absolute;left:0;top:928px;width:1200px;height:396px;overflow:hidden;
  background:linear-gradient(90deg,#e7eef6 0%,#ecf1f6 65%,#e6ebf0 100%)}
.products .photo{left:820px;top:0;width:380px;height:396px;
  background:
    linear-gradient(115deg,rgba(255,255,255,0) 35%,rgba(255,255,255,.85) 52%,rgba(205,212,220,.5) 62%,rgba(255,255,255,0) 75%),
    linear-gradient(180deg,rgba(236,241,246,0) 55%,rgba(228,222,210,.6) 100%),
    linear-gradient(90deg,rgba(236,241,246,0) 0%,#e3e8ee 40%,#dfe4ea 100%)}
.products .section-title{position:absolute;left:132px;top:42px}
.products .arrow{position:absolute;left:886px;top:44px}
.card{position:absolute;top:86px;width:219px;text-align:center}
.card .shot{height:139px;background:var(--white);position:relative}
.card .shot i{position:absolute;left:64px;top:44px;width:90px;height:52px;border-radius:50%;
  background:linear-gradient(180deg,#f3f3f3,#d8d8d8)}
.card h4{font-weight:400;font-size:11.5px;margin-top:18px;color:#333}
.card .price{font-size:24px;margin-top:6px;color:#222}
.card p{font-size:9px;color:#777;line-height:13.5px;margin-top:6px;padding:0 4px}

/* testimonials */
.testimonials{position:absolute;left:0;top:1324px;width:1200px;height:370px;background:linear-gradient(90deg,#f6f6f6,#f4f4f4);overflow:hidden}
.testimonials .photo{left:0;top:0;width:440px;height:370px;
  background:
    linear-gradient(100deg,rgba(230,190,165,0) 0%,rgba(230,190,165,0) 10%,rgba(226,184,158,.9) 22%,rgba(240,210,190,.85) 45%,rgba(246,246,246,0) 85%),
    linear-gradient(180deg,rgba(246,246,246,.8) 0%,rgba(246,246,246,0) 30%,rgba(246,246,246,0) 80%,rgba(246,246,246,.9) 100%)}
.testimonials .section-title{position:absolute;right:133px;top:98px}
.testimonials blockquote{position:absolute;right:133px;top:138px;width:560px;text-align:right;font-size:12.5px;line-height:23px;color:#666}
.testimonials cite{position:absolute;right:133px;top:214px;font-style:normal;font-size:13.5px;color:#333}
.ring-dots{position:absolute;left:983px;top:258px;display:flex;gap:12px}
.ring-dots span{width:9px;height:9px;border-radius:50%;border:1px solid #999}
.ring-dots span.on{background:#999}

/* about */
.about{position:absolute;left:0;top:1694px;width:1200px;height:400px;background:linear-gradient(180deg,#efefef,#e4e4e4);overflow:hidden}
.about .photo{left:760px;top:0;width:440px;height:400px;
  background:
    linear-gradient(125deg,rgba(255,255,255,0) 30%,rgba(255,255,255,.9) 45%,rgba(180,180,180,.6) 55%,rgba(255,255,255,0) 68%),
    linear-gradient(90deg,rgba(236,236,236,0) 0%,#e2e2e2 35%,#d9d9d9 100%)}
.about .section-title{position:absolute;left:132px;top:52px}
.about p{position:absolute;left:132px;top:101px;width:585px;font-size:12px;line-height:20px;color:#777;text-align:justify}
.btn-white{position:absolute;background:var(--white);font-size:10.5px;color:#666;display:flex;align-items:center;justify-content:center;letter-spacing:.3px}
.about .btn-white{left:132px;top:299px;width:97px;height:39px}

/* partners */
.partners{position:absolute;left:0;top:2094px;width:1200px;height:129px;background:var(--white);display:flex;align-items:center;justify-content:space-between;padding:0 132px}
.partners span{font-size:12.5px;color:#444}

/* banner */
.banner{position:absolute;left:0;top:2223px;width:1200px;height:233px;
  background:
    linear-gradient(120deg,rgba(255,255,255,0) 20%,rgba(255,255,255,.08) 30%,rgba(255,255,255,0) 40%,rgba(255,255,255,.07) 60%,rgba(255,255,255,0) 70%),
    linear-gradient(180deg,#3a3a3a 0%,#262626 60%,#151515 100%)}
.banner h2{position:absolute;left:0;width:1200px;top:66px;text-align:center;color:var(--white);font-weight:700;font-size:32px;letter-spacing:.5px}
.banner .btn-white{left:551px;top:118px;width:96px;height:39px}

/* footer */
.footer{position:absolute;left:0;top:2456px;width:1200px;height:196px;background:linear-gradient(180deg,#f3f3f3,#fafafa)}
.fcol{position:absolute;top:28px}
.fcol h5{font-weight:400;font-size:12.5px;color:#333;margin-bottom:14px}
.divider{position:absolute;top:28px;width:1px;height:140px;background:var(--line)}
.social{display:grid;grid-template-columns:70px 70px;gap:8px 4px}
.social span{display:flex;align-items:center;gap:5px;font-size:10px;color:#444}
.social span:before{content:"";width:12px;height:12px;border-radius:50%;background:#5a5a5a;flex:none}
.field{width:170px;height:31px;background:var(--white);border:1px solid #ddd;font-size:10px;color:#aaa;display:flex;align-items:center;justify-content:space-between;padding:0 10px}
.fcol ul{list-style:none;font-size:10px;color:#555;line-height:20.5px}
.fcol ul li:before{content:"•";color:#999;margin-right:6px}
.gift b{display:block;font-weight:400;font-size:11px;color:#333;margin-bottom:6px}
.gift p{width:255px;font-size:9px;line-height:16px;color:#888}
.copyright{position:absolute;left:0;top:2652px;width:1200px;height:51px;background:#e4e4e4;text-align:center;font-size:11px;line-height:51px;color:#555}
</style>
</head>
<body>

<nav class="topnav">
  <div class="links">
    <span class="active">Home</span><span>How it Works</span><span>Diamond Gallery</span><span>About</span><span>FAQs</span><span>Contact us</span>
  </div>
  <div class="cart">My Cart - $00.00
    <svg width="14" height="18" viewBox="0 0 14 18"><path d="M1 5h12v12H1z" fill="none" stroke="#444" stroke-width="1.3"/><path d="M4 7V4a3 3 0 016 0v3" fill="none" stroke="#444" stroke-width="1.3"/></svg>
  </div>
</nav>

<header class="hero">
  <div class="photo" role="img" aria-label="Close-up of a diamond solitaire engagement ring with a gold pavé band"></div>
  <div class="brandbox">
    <div class="mark"></div>
    <div class="name">The Velvet<br>Pathfinder</div>
  </div>
  <h1>Suspendisse suscipit<br>pulvinar hendrerit</h1>
  <div class="btn-dark">Find Engagement Ring</div>
  <div class="dots"><span></span><span></span><span class="on"></span><span></span></div>
</header>

<section class="how">
  <div class="photo" role="img" aria-label="Tweezers holding a loose diamond above scattered stones"></div>
  <div class="section-title">How it works</div>
  <p class="lead">Integer arcu eros, interdum ut libero ac, consequat consequat ex. Mauris condimentum dui ex, accumsan congue leo rutrum tempus.</p>
  <div class="step" style="top:108px">
    <div class="icon"><svg width="24" height="24" viewBox="0 0 24 24"><rect x="3" y="5" width="15" height="15" rx="2" fill="none" stroke="#fff" stroke-width="2"/><path d="M10 14l9-9 2 2-9 9h-2z" fill="#fff"/></svg></div>
    <div><h3>DETERMINE YOUR STYLE, BUDGET, CATGORY</h3><p>Fusce efficitur urna at mi interdum, eget hendrerit purus eleifend</p></div>
  </div>
  <div class="step" style="top:200px">
    <div class="icon"><svg width="24" height="24" viewBox="0 0 24 24"><path d="M3 8h4l2-3h6l2 3h4v12H3z" fill="#fff"/><circle cx="12" cy="13.5" r="4" fill="#555"/><circle cx="12" cy="13.5" r="2.3" fill="#fff"/></svg></div>
    <div><h3>UPLOAD DESIGN/PHOTO</h3><p>Fusce efficitur urna at mi interdum, eget hendrerit purus eleifend</p></div>
  </div>
  <div class="step" style="top:292px">
    <div class="icon"><svg width="24" height="24" viewBox="0 0 24 24"><path d="M12 2l9 5v10l-9 5-9-5V7z" fill="#fff"/><path d="M3 7l9 5 9-5M12 12v10" fill="none" stroke="#555" stroke-width="1.5"/></svg></div>
    <div><h3>GET YOUR RING AS SOON AS POSSIBLE</h3><p>Fusce efficitur urna at mi interdum, eget hendrerit purus eleifend</p></div>
  </div>
</section>

<section class="products">
  <div class="photo" role="img" aria-label="Emerald-cut diamond ring resting on soft fabric"></div>
  <div class="section-title">Our products</div>
  <svg class="arrow" width="16" height="14" viewBox="0 0 16 14"><path d="M1 7h13M9 2l5 5-5 5" fill="none" stroke="#333" stroke-width="1.4"/></svg>
  <div class="card" style="left:132px">
    <div class="shot" role="img" aria-label="Diamond ring with pavé band"><i></i></div>
    <h4>SED ODIO NISL, ULTRICIES EGET</h4><div class="price">$0,000.00</div>
    <p>Fusce efficitur urna at mi interdum, eget hendrerit purus eleifend. Suspendisse pulvinar accumsan mi eget ornare. Donec pulvinar elit sit amet.</p>
  </div>
  <div class="card" style="left:409px">
    <div class="shot" role="img" aria-label="Solitaire diamond ring in white gold"><i></i></div>
    <h4>SED ODIO NISL, ULTRICIES EGET</h4><div class="price">$0,000.00</div>
    <p>Fusce efficitur urna at mi interdum, eget hendrerit purus eleifend. Suspendisse pulvinar accumsan mi eget ornare. Donec pulvinar elit sit amet.</p>
  </div>
  <div class="card" style="left:683px">
    <div class="shot" role="img" aria-label="Slim diamond ring shown upright"><i></i></div>
    <h4>SED ODIO NISL, ULTRICIES EGET</h4><div class="price">$0,000.00</div>
    <p>Fusce efficitur urna at mi interdum, eget hendrerit purus eleifend. Suspendisse pulvinar accumsan mi eget ornare. Donec pulvinar elit sit amet.</p>
  </div>
</section>

<section class="testimonials">
  <div class="photo" role="img" aria-label="Two hands held together, one wearing an engagement ring"></div>
  <div class="section-title">Testimonials</div>
  <blockquote>Mauris condimentum dui ex, accumsan congue leo rutrum tempus. Nullam aliquam leo porttitor metus accumsan, aliquet vestibulum mauris tincidunt. Donec gravida, ligula ornare scelerisque pretium, odio dolor scelerisque sem, eu tempus sapien erat et diam.</blockquote>
  <cite>John Cole, City</cite>
  <div class="ring-dots"><span class="on"></span><span></span><span></span><span></span></div>
</section>

<section class="about">
  <div class="photo" role="img" aria-label="Ornate diamond ring in close-up"></div>
  <div class="section-title">About The Velvet Pathfinder</div>
  <p>Phasellus non neque at risus auctor laoreet a ut velit. Sed odio nisl, ultricies eget congue in, varius id sem. Phasellus at orci a mauris gravida bibendum. Integer quis lacus eu enim ornare condimentum. Integer varius, ex a ullamcorper ullamcorper, metus ante facilisis enim, at tempus justo nisi sed diam. Sed tempor tincidunt luctus. Cras vel elit at lorem consequat pulvinar eget quis purus. Nulla pharetra ullamcorper dictum. Fusce efficitur urna at mi interdum, eget hendrerit purus eleifend. Suspendisse pulvinar accumsan mi eget ornare. Donec pulvinar elit sit amet tempor luctus. Ut et gravida quam. Nunc dolor massa, semper et dapibus ac, maximus eu mauris. Nunc dictum augue sed velit vehicula bibendum. Etiam a feugiat nisi. Cras ac vestibulum nisl.</p>
  <div class="btn-white">READ MORE</div>
</section>

<section class="partners">
  <span>Noemi Keller</span><span>Ivory Lane</span><span>Clara Bellamy</span><span>Harlow &amp; Vance</span><span>Delia Marsh</span><span>Little Sprout Co</span><span>Sofia Renard</span>
</section>

<section class="banner" role="img" aria-label="Dark background of scattered loose diamonds">
  <h2>PHASELLUS NEQUE RISUS AUCTOR LAOREET</h2>
  <div class="btn-white">READ MORE</div>
</section>

<footer class="footer">
  <div class="fcol" style="left:132px"><h5>Follow us on</h5>
    <div class="social"><span>Pathway</span><span>Glint</span><span>Linkly</span><span>Circlet</span></div></div>
  <div class="divider" style="left:290px"></div>
  <div class="fcol" style="left:308px"><h5>Newsletter Subscribe</h5>
    <div class="field">Email ID<svg width="14" height="10" viewBox="0 0 14 10"><rect x=".5" y=".5" width="13" height="9" fill="#bbb"/><path d="M.5 .5l6.5 5 6.5-5" fill="none" stroke="#fff"/></svg></div>
  </div>
  <div class="divider" style="left:520px"></div>
  <div class="fcol" style="left:542px"><h5>Links</h5>
    <ul><li>Home</li><li>How it Works</li><li>Diamond Gallery</li><li>About</li><li>FAQs</li><li>Contact us</li></ul></div>
  <div class="divider" style="left:668px"></div>
  <div class="fcol" style="left:694px"><h5>Cart</h5>
    <ul><li>My Account</li><li>My Cart</li><li>Checkout</li><li>Login</li></ul></div>
  <div class="divider" style="left:793px"></div>
  <div class="fcol gift" style="left:813px"><h5>Gift</h5>
    <b>Suspendisse pulvinar accumsan</b>
    <p>Donec gravida, ligula ornare scelerisque pretium, odio dolor scelerisque sem, eu tempus sapien erat et diam. Donec efficitur blandit neque et mollis. Donec a placerat augue, vel rhoncus eros. Vivamus ullamcorper est eget orci porta, vitae tempor elit elementum.</p>
  </div>
</footer>

<div class="copyright">Copyright © 2016 The Velvet Pathfinder. All rights reserved</div>

</body>
</html>
```